Design Creative Banner or Gif Ads. 3 Designs To Be Selected

Come up with some creative banner ads for stonewell.co.nz

*At least 3 different winning banners will be chosen*

Please provide banner ads / gif ads in common google ads / website banner formats.

They can be gif or static but must stand out while still maintaining clear clean text and visuals, with a premium professional feel (please avoid clip art or anything that gives a cheap message).

Please keep in mind that these will likely be small ads so text needs to be large and if there's there a lot of text then use multiple frames/ pages as submit as a gif.

Style
Minimal & clean lines
Architectural or realistic images
Avoid cartoon styles, clipart, or anything that looks cheap

Font
Nexa or Montserrat or similar

Tone
Premium, serious, trustworthy — fits new builds

Colours
Option 1: Deep Navy (trust & quality) & lighter blues and warm grey
Option 2: Open to bright colours to help the ads stand out, such as (but not limited to) bright pink with black, yellow, fluorescent green, provided the messaging is still done professionally.
Our logo is attached (Stone Well Logo)

Display Sizes
Ad specs for file sizes should be file formats like JPEG, GIF, and PNG, with animations limited to a max of 30 seconds or less.
We will need several different ad sizes provided for each of the 3 selected winning designs.

• Medium Rectangle: 300 × 250 pixels
• Leaderboard: 728 × 90 pixels
• Desktop Banner ad image: (640x360 pixels)
• Desktop Banner ad image 2: (300x600 pixels)
• Possibly one or two other sizes

Flexibility to be creative
The ad text, words, upper/lower case, layout, colour, theme, and images can be adjusted to how you think it will look best. The follow example ads are just examples of what we are after but we are keen to see what you can create.

Recommendations at this point:
1. Avoid text heavy
2. Looking for more Gif ads
3. Imaging: if possible use real stock photo's rather than AI

Themes:

1
Building Soon? Start Here
Free Build Planning Pack:
✓ Build Cost Calculator
✓ Hidden Cost Checklist
✓ Builder Comparison Guide
Build With Confidence
Download Free

2
Before You Choose A Builder
Compare Price, Scope, Risk & Value
Avoid Costly Mistakes
Choose The Right Builder With Confidence
Download The Free Guide

3
Planning A New Build?
Avoid These Common Mistakes:
✗ Hidden Exclusions
✗ Missing Scope
✗ Unrealistic Allowances
✗ Budget Blowouts
Download The Free Guide

4
Before You Buy Land
Know what it could cost to build.
Avoid Costly Building Mistakes
Download Our Free Guides

5
Know Your Build Budget?
• Free Build Cost Calculator
• Hidden Cost Checklist
• Build Planning Tools
Calculate Costs (Download)

Target Market(s)

Landowners looking to build

Industry/Entity Type

Building

Font styles to use
Other font styles liked:
• Nexa or Montserrat or similar

Requirements
Should not have
• Avoid cartoon styles, clipart, or anything that looks cheap

```html
<!DOCTYPE html>
<html lang="en">
<head>
<meta charset="utf-8">
<title>Stone Well – Banner Ads</title>
<link href="https://fonts.googleapis.com/css2?family=Montserrat:ital,wght@0,400;0,500;0,600;0,700;0,800;1,500;1,600&display=swap" rel="stylesheet">
<style>
  :root{
    --navy:#163652;
    --navy-deep:#0f2740;
    --blue:#2f95c9;
    --blue-light:#4fb0e0;
    --head-blue:#1f6e9a;
    --ink:#1b2330;
    --paper:#ffffff;
    --dusk-sky:#1a2636;
    --dusk-glow:#e7b56a;
    --facade:#ece6da;
    --sky:#6f9fd0;
    --cloud:#e8eef4;
    --timber:#8a5a36;
    --lawn:#5f8a3e;
    --sunset:#d7a9b8;
  }
  *{box-sizing:border-box;margin:0;padding:0}
  html,body{width:1200px;height:811px;overflow:hidden;background:var(--paper)}
  body{position:relative;font-family:"Montserrat",Arial,sans-serif;color:var(--ink)}
  .ad{position:absolute;overflow:hidden;background:var(--paper);box-shadow:0 1px 5px rgba(0,0,0,.28)}
  .brand{position:absolute;display:flex;flex-direction:column;justify-content:center}
  .brand-name{display:flex;align-items:center;gap:8px;font-weight:600;color:var(--navy);letter-spacing:.2px}
  .brand-square{background:var(--navy);display:block}
  .brand-tag{font-weight:700;color:var(--blue);text-transform:uppercase;letter-spacing:.3px}
  .photo{position:absolute}
  .abs{position:absolute;white-space:nowrap}
  .btn{position:absolute;display:flex;align-items:center;color:#fff;font-weight:600}
  .checks{position:absolute;list-style:none}
  .checks li{display:flex;align-items:center}
  .chev{flex:none}

  /* Skyscraper 300x600 */
  .ad-tall{left:20px;top:30px;width:362px;height:720px}
  .ad-tall .brand{left:0;right:0;top:0;height:72px;align-items:center}
  .ad-tall .brand-name{font-size:25px}
  .ad-tall .brand-square{width:22px;height:22px}
  .ad-tall .brand-tag{font-size:6.5px;margin-top:2px}
  .ad-tall .photo{left:0;top:72px;width:362px;height:310px;
    background:
      radial-gradient(ellipse 46% 30% at 50% 48%, var(--dusk-glow) 0%, rgba(231,181,106,.55) 45%, rgba(231,181,106,0) 100%),
      radial-gradient(ellipse 70% 42% at 50% 46%, var(--facade) 0%, rgba(236,230,218,.35) 55%, rgba(236,230,218,0) 100%),
      linear-gradient(180deg, var(--dusk-sky) 0%, #2c3a4c 30%, #3b3f45 70%, #2a2a2c 100%)}
  .ad-tall .panel{position:absolute;left:0;top:0;width:362px;height:720px}
  .ad-tall .headline{left:0;right:0;top:386px;text-align:center;font-size:34px;font-weight:700;color:#fff}
  .ad-tall .sub{left:49px;top:436px;font-size:12.5px;font-weight:500;color:#fff}
  .ad-tall .checks{left:49px;top:458px}
  .ad-tall .checks li{height:41px;font-size:19px;font-weight:500;color:#fff;gap:12px}
  .ad-tall .guide{left:49px;top:584px;font-size:15px;font-style:italic;font-weight:500;color:#fff}
  .ad-tall .btn{left:49px;top:627px;width:121px;height:29px;font-size:13px;padding-left:6px}
  .ad-tall .foot{left:0;right:0;top:682px;height:38px;background:var(--paper);display:flex;align-items:center;justify-content:center;font-size:10.5px;font-weight:500;color:var(--ink)}

  /* Desktop 640x360 */
  .ad-wide{left:407px;top:30px;width:769px;height:432px}
  .ad-wide .left-bg{position:absolute;left:0;top:0;width:404px;height:432px;
    background:
      radial-gradient(ellipse 60% 30% at 60% 85%, rgba(170,190,160,.45) 0%, rgba(170,190,160,0) 100%),
      linear-gradient(180deg,#f4f6f8 0%,#e9eef1 55%,#dde6e8 100%)}
  .ad-wide .brand{left:0;top:10px;width:359px;height:76px;background:var(--paper);padding-left:28px}
  .ad-wide .brand-name{font-size:33px}
  .ad-wide .brand-square{width:28px;height:28px}
  .ad-wide .brand-tag{font-size:8.5px;margin-top:2px}
  .ad-wide .photo{left:404px;top:0;width:365px;height:432px;
    background:
      radial-gradient(ellipse 40% 12% at 80% 22%, var(--cloud) 0%, rgba(232,238,244,0) 100%),
      radial-gradient(ellipse 26% 40% at 45% 52%, rgba(138,90,54,.85) 0%, rgba(138,90,54,0) 100%),
      radial-gradient(ellipse 60% 42% at 55% 55%, var(--facade) 0%, rgba(236,230,218,.6) 55%, rgba(236,230,218,0) 100%),
      linear-gradient(180deg, var(--sky) 0%, #a9c5e0 25%, #c8ccd0 45%, #6e6a66 72%, var(--lawn) 84%, #9ca79a 100%)}
  .ad-wide .headline{left:42px;top:144px;font-size:41px;font-weight:700;color:var(--head-blue)}
  .ad-wide .sub{left:44px;top:212px;font-size:16px;font-weight:700;line-height:25px;color:var(--ink)}
  .ad-wide .guide{left:44px;top:282px;font-size:16px;font-style:italic;font-weight:600;color:#333b45}
  .ad-wide .btn{left:46px;top:336px;width:116px;height:28px;font-size:13px;padding-left:16px}

  /* Medium rectangle 300x250 */
  .ad-rect{left:407px;top:480px;width:361px;height:301px}
  .ad-rect .brand{left:18px;top:6px;height:34px}
  .ad-rect .brand-name{font-size:17px;gap:6px}
  .ad-rect .brand-square{width:15px;height:15px}
  .ad-rect .brand-tag{font-size:4.6px}
  .ad-rect .roof{position:absolute;left:174px;top:28px}
  .ad-rect .headline{left:19px;top:64px;font-size:17px;font-weight:700;color:var(--blue)}
  .ad-rect .sub{left:19px;top:97px;font-size:9px;font-weight:700;line-height:13px;color:var(--ink)}
  .ad-rect .checks{left:19px;top:135px}
  .ad-rect .checks li{height:28px;font-size:9.8px;font-weight:500;gap:8px}
  .ad-rect .btn{left:19px;top:229px;width:88px;height:21px;font-size:8px;padding-left:7px}
  .ad-rect .foot{left:19px;top:267px;font-size:9.2px;font-weight:500;line-height:12px}
</style>
</head>
<body>

<!-- 300 x 600 skyscraper -->
<section class="ad ad-tall">
  <div class="brand">
    <div class="brand-name"><span class="brand-square"></span>Stone Well</div>
    <div class="brand-tag">Compare quotes from trusted builders</div>
  </div>
  <div class="photo" role="img" aria-label="Two-storey modern white home lit warmly at dusk with a front driveway"></div>
  <svg class="panel" width="362" height="720" viewBox="0 0 362 720" aria-hidden="true">
    <polygon points="0,300 181,372 362,300 362,720 0,720" fill="var(--navy)"/>
    <polygon points="0,318 181,386 362,318 362,720 0,720" fill="var(--navy-deep)" opacity=".35"/>
    <polygon points="0,292 181,362 362,292 362,306 181,378 0,306" fill="var(--blue)"/>
    <polygon points="0,283 181,352 362,283 362,292 181,362 0,292" fill="var(--paper)"/>
  </svg>
  <h2 class="abs headline">Bought Land?</h2>
  <p class="abs sub">Before You Choose A &nbsp;Builder, Read This.</p>
  <ul class="checks">
    <li><svg class="chev" width="14" height="12" viewBox="0 0 14 12" aria-hidden="true"><path d="M1 1l5 5-5 5M7 1l5 5-5 5" fill="none" stroke="#fff" stroke-width="2.2"/></svg>Avoid Costly Mistakes</li>
    <li><svg class="chev" width="14" height="12" viewBox="0 0 14 12" aria-hidden="true"><path d="M1 1l5 5-5 5M7 1l5 5-5 5" fill="none" stroke="#fff" stroke-width="2.2"/></svg>Budget Blowouts</li>
    <li><svg class="chev" width="14" height="12" viewBox="0 0 14 12" aria-hidden="true"><path d="M1 1l5 5-5 5M7 1l5 5-5 5" fill="none" stroke="#fff" stroke-width="2.2"/></svg>Contract Surprises.</li>
  </ul>
  <p class="abs guide">Free Build Planning Guide</p>
  <svg class="abs" style="left:49px;top:627px" width="121" height="29" viewBox="0 0 121 29" aria-hidden="true">
    <polygon points="0,0 108,0 121,14.5 108,29 0,29" fill="var(--blue)"/>
  </svg>
  <div class="btn">Download Now</div>
  <div class="abs foot">Choose The Right Builder With Clarity &amp; Confidence. Stone Well</div>
</section>

<!-- 640 x 360 desktop banner -->
<section class="ad ad-wide">
  <div class="left-bg" role="img" aria-label="Faded view of a modern home garden with stepping stone path"></div>
  <div class="photo" role="img" aria-label="Contemporary gabled home with timber cladding, large windows and green lawn"></div>
  <div class="brand">
    <div class="brand-name"><span class="brand-square"></span>Stone Well</div>
    <div class="brand-tag">Compare quotes from trusted builders</div>
  </div>
  <h2 class="abs headline">Bought Land?</h2>
  <p class="abs sub">Understand The Steps To Building<br>Your New Home</p>
  <p class="abs guide">Free Build Roadmap</p>
  <svg class="abs" style="left:46px;top:336px" width="118" height="28" viewBox="0 0 118 28" aria-hidden="true">
    <polygon points="0,0 100,0 112,14 100,28 0,28" fill="var(--navy)"/>
    <polygon points="100,0 106,0 118,14 106,28 100,28 112,14" fill="var(--blue-light)"/>
  </svg>
  <div class="btn">Download</div>
</section>

<!-- 300 x 250 medium rectangle -->
<section class="ad ad-rect">
  <div class="brand">
    <div class="brand-name"><span class="brand-square"></span>Stone Well</div>
    <div class="brand-tag">Compare quotes from trusted builders</div>
  </div>
  <svg class="roof" width="187" height="273" viewBox="0 0 187 273">
    <defs>
      <linearGradient id="rectSky" x1="0" y1="0" x2="0" y2="1">
        <stop offset="0" stop-color="var(--sunset)"/>
        <stop offset=".3" stop-color="#e9e3e2"/>
        <stop offset=".62" stop-color="#8a8580"/>
        <stop offset=".8" stop-color="#c9c7c2"/>
        <stop offset="1" stop-color="#6f8a5a"/>
      </linearGradient>
      <radialGradient id="rectFacade" cx=".45" cy=".42" r=".45">
        <stop offset="0" stop-color="#f4f1ec"/>
        <stop offset=".6" stop-color="#f4f1ec" stop-opacity=".55"/>
        <stop offset="1" stop-color="#f4f1ec" stop-opacity="0"/>
      </radialGradient>
      <radialGradient id="rectTimber" cx=".62" cy=".5" r=".22">
        <stop offset="0" stop-color="var(--timber)" stop-opacity=".85"/>
        <stop offset="1" stop-color="var(--timber)" stop-opacity="0"/>
      </radialGradient>
    </defs>
    <polygon points="0,40 94,2 187,40 187,273 0,273" fill="var(--navy)"/>
    <g role="img" aria-label="Modern white two-storey home with timber entry and concrete path at sunset">
      <polygon points="0,52 94,14 187,52 187,273 0,273" fill="url(#rectSky)"/>
      <polygon points="0,52 94,14 187,52 187,273 0,273" fill="url(#rectFacade)"/>
      <polygon points="0,52 94,14 187,52 187,273 0,273" fill="url(#rectTimber)"/>
    </g>
  </svg>
  <h2 class="abs headline">BOUGHT LAND?</h2>
  <p class="abs sub">Avoid Costly Build Mistakes<br>Discover The Hidden Costs</p>
  <ul class="checks">
    <li><svg class="chev" width="11" height="9" viewBox="0 0 11 9" aria-hidden="true"><path d="M1 .8l3.7 3.7L1 8.2M5.5 .8l3.7 3.7-3.7 3.7" fill="none" stroke="var(--blue)" stroke-width="1.8"/></svg>Build Cost Calculator</li>
    <li><svg class="chev" width="11" height="9" viewBox="0 0 11 9" aria-hidden="true"><path d="M1 .8l3.7 3.7L1 8.2M5.5 .8l3.7 3.7-3.7 3.7" fill="none" stroke="var(--blue)" stroke-width="1.8"/></svg>Build Journey Roadmap</li>
    <li><svg class="chev" width="11" height="9" viewBox="0 0 11 9" aria-hidden="true"><path d="M1 .8l3.7 3.7L1 8.2M5.5 .8l3.7 3.7-3.7 3.7" fill="none" stroke="var(--blue)" stroke-width="1.8"/></svg>Hidden Cost Checklist</li>
  </ul>
  <svg class="abs" style="left:19px;top:229px" width="90" height="21" viewBox="0 0 90 21" aria-hidden="true">
    <polygon points="0,0 76,0 84,10.5 76,21 0,21" fill="var(--navy)"/>
    <polygon points="76,0 82,0 90,10.5 82,21 76,21 84,10.5" fill="var(--blue-light)"/>
  </svg>
  <div class="btn">Download Free</div>
  <p class="abs foot">Choose The Right Builder With<br>Clarity &amp; Confidence. Stone Well</p>
</section>

</body>
</html>
```